Website for keystone mobile detailing.

Need a homepage, pages for: car and truck detailing, boat detailing, airplane detailing, about us, contact us. I have the domain name through nimbuspark so I will need the design uploaded on my domain. Also hoping to link other domains to this page.I would like to see the logo more pronounced. I would like to see a large phone number link to call my business. The layout looks nice but the pics need to depict car washing and waxing not car mechanics. i would like the colors of the webpage to incorporate the colors found in the logo in some way. I would like links to social media pages

Target Market(s)

Local customers in Vero Beach, Florida.

Number of Pages Required

5+ page

Colors

Designer to choose colors to be used in the design.

Requirements
Must have
• Easy to navigate, attractive pages with pictures and logo, professional looking. must have my phone number and logo very prevalent and links to call or go to home page. I would like links to my social media accounts on the home page.
Nice to have
• Easy to navigate, attractive pages with pictures and logo, professional looking.

```html
<!DOCTYPE html>
<html lang="en">
<head>
<meta charset="utf-8">
<title>Keystone Mobile Detailing</title>
<link href="https://fonts.googleapis.com/css2?family=Open+Sans:wght@400;600;700&family=PT+Sans:wght@400;700&family=Roboto+Slab:wght@500&display=swap" rel="stylesheet">
<style>
:root{
  --navy:#1b1e7c;
  --navy-dark:#15186a;
  --sky:#12a4e8;
  --red:#e3262d;
  --ink:#333;
  --muted:#555;
  --band:#f3f2f2;
  --footer:#111111;
  --footer-2:#161616;
  --footer-3:#262626;
  --white:#fff;
}
*{box-sizing:border-box;margin:0;padding:0}
html,body{width:1200px;height:2853px;overflow:hidden}
body{position:relative;background:var(--white);font-family:"PT Sans",sans-serif;color:var(--ink)}
.abs{position:absolute}
a{color:inherit;text-decoration:none}

/* header */
.logo{left:200px;top:14px;width:210px;height:66px;display:block}
.logo-dot{position:absolute;left:0;top:6px;width:20px;height:20px;border-radius:50%;background:var(--red)}
.logo-name{position:absolute;left:28px;top:2px;font:700 19px/21px "Open Sans",sans-serif;color:var(--navy);white-space:nowrap}
.logo-phone{position:absolute;left:58px;top:49px;font:700 12px/12px "Open Sans",sans-serif;color:var(--red);letter-spacing:1px;white-space:nowrap}
.contact-item{top:28px;display:flex;align-items:center;gap:14px}
.icon-circle{width:30px;height:30px;border-radius:50%;background:var(--navy);display:flex;align-items:center;justify-content:center;flex:none}
.contact-label{font:700 12px/16px "Open Sans",sans-serif;color:var(--ink)}
.contact-value{font:400 12px/16px "Open Sans",sans-serif;color:var(--ink);white-space:nowrap}
.divider-v{left:620px;top:28px;width:2px;height:32px;background:var(--navy)}
.socials{left:902px;top:32px;display:flex;gap:6px}
.socials span{width:20px;height:20px;border-radius:50%;background:var(--navy)}

/* nav */
.nav{left:200px;top:89px;width:800px;height:46px;background:var(--sky);display:flex;z-index:2}
.nav-home{width:44px;background:var(--navy-dark);display:flex;align-items:center;justify-content:center}
.nav a{font:700 13px/46px "Open Sans",sans-serif;color:var(--white);padding:0 18px}
.nav a.active{background:var(--navy-dark);padding:0 12px}
.nav-search{margin-left:auto;width:48px;background:var(--navy-dark);display:flex;align-items:center;justify-content:center}

/* hero */
.hero{left:0;top:106px;width:1200px;height:552px;background:linear-gradient(100deg,#3b3a38 0%,#5b5a56 40%,#2a2b2d 75%,#45454a 100%)}
.hero-title{right:200px;top:270px;text-align:right;font:700 50px/54px "Open Sans",sans-serif;color:var(--white)}
.hero-text{right:200px;top:398px;width:530px;text-align:right;font:400 14.5px/22px "PT Sans",sans-serif;color:var(--white)}
.btn{background:linear-gradient(#3c40c0,#23268e);color:var(--white);font:700 12px/1 "Open Sans",sans-serif;text-transform:uppercase;display:flex;align-items:center;justify-content:center;border-radius:4px}
.hero-btn{left:865px;top:472px;width:134px;height:46px}
.hero-arrow{top:559px;width:28px;height:28px;border-radius:50%;background:var(--white);display:flex;align-items:center;justify-content:center}

/* about */
.about-kicker{left:200px;top:760px;font:400 15px/18px "Open Sans",sans-serif;color:var(--red);white-space:nowrap}
.about-rule{left:378px;top:769px;width:142px;height:1px;background:#888}
.section-title-left{left:200px;top:795px;font:700 38px/44px "Open Sans",sans-serif;color:#1d1d1d}
.about-text{left:200px;top:848px;width:360px;font:400 12.5px/23px "PT Sans",sans-serif;color:var(--muted)}
.about-photo{left:599px;top:723px;width:400px;height:306px;background:linear-gradient(160deg,#b8c4d0,#6f8096 55%,#2d3b52)}
.read-more{left:862px;top:987px;width:137px;height:42px;background:var(--white);display:flex;align-items:center;justify-content:center;gap:10px;font:600 12px/1 "Open Sans",sans-serif;color:var(--ink)}

/* services */
.services-band{left:0;top:1094px;width:1200px;height:274px;background:var(--band)}
.section-title{left:0;width:1200px;text-align:center;font:700 38px/44px "Open Sans",sans-serif;color:var(--navy)}
.section-sub{left:230px;width:740px;text-align:center;font:400 12.5px/21px "PT Sans",sans-serif;color:var(--muted)}
.grid{left:217px;top:1276px;width:766px;height:284px;display:grid;grid-template-columns:repeat(3,1fr);grid-template-rows:repeat(2,1fr);background:var(--white);box-shadow:0 0 0 1px #e4e4e4}
.tile-photo{width:100%;height:100%}
.tile-text{padding:30px 18px 0;text-align:center;background:var(--white)}
.tile-text h3{font:500 15px/18px "Roboto Slab",serif;color:#222;margin-bottom:8px}
.tile-text p{font:400 12.5px/17px "PT Sans",sans-serif;color:#333}
.tile-text .more{display:inline-block;margin-top:6px;font:600 10px/1 "Open Sans",sans-serif;color:var(--sky)}
.services-btn{left:517px;top:1619px;width:166px;height:45px}

/* testimonials */
.testi-band{left:0;top:1729px;width:1200px;height:386px;background:linear-gradient(#f2f1f1,#eceaea)}
.card{top:1883px;width:257px;height:160px;background:var(--white);border:1px solid #e59a9a;text-align:center;padding:50px 22px 0}
.card p{font:400 12.5px/18px "PT Sans",sans-serif;color:#777}
.card .by{margin-top:12px;display:flex;justify-content:center;align-items:center;gap:12px;font:700 12px/1 "PT Sans",sans-serif;color:#222}
.stars{display:flex;gap:1px}
.avatar{top:1856px;width:54px;height:54px;border-radius:50%;background:linear-gradient(#d9d4d0,#a9a4a0);border:3px solid var(--white)}
.dots{left:583px;top:2075px;display:flex;gap:5px}
.dots span{width:8px;height:8px;border-radius:50%;background:#9aa}
.dots span.on{background:var(--navy)}

/* clients */
.client{top:2245px;width:137px;height:85px;background:var(--white);border:1px solid #e6e6e6;display:flex;align-items:center;justify-content:center;gap:6px;font:700 18px/1 "Open Sans",sans-serif;color:#1d1d1d}
.client i{width:14px;height:14px;background:#1d1d1d;display:block}
.client-arrow{top:2275px;width:22px;height:22px;border:1px solid #bbb;display:flex;align-items:center;justify-content:center}

/* footer */
.footer{left:0;top:2389px;width:1200px;height:259px;background:var(--footer)}
.foot-col{top:2446px}
.foot-col h4{font:700 13px/16px "Open Sans",sans-serif;color:var(--white);margin-bottom:24px;text-transform:uppercase}
.foot-col li{list-style:none;font:400 12px/24px "Open Sans",sans-serif;color:#ddd}
.newsletter{left:736px;top:2496px;width:263px;height:45px;border:1px solid #888;display:flex;align-items:center;justify-content:space-between;padding:0 14px;font:400 12px/1 "Open Sans",sans-serif;color:#ddd}
.foot-social{left:885px;top:2556px;display:flex;gap:18px}
.foot-social span{width:11px;height:11px;border-radius:50%;background:#ddd}
.contact-row{left:0;top:2648px;width:1200px;height:154px;background:var(--footer-2);border-top:1px solid #333}
.cinfo{top:2690px;width:300px;text-align:center;font:400 12px/16px "Open Sans",sans-serif;color:#ddd}
.cinfo svg{display:block;margin:0 auto 14px}
.copy{left:0;top:2802px;width:1200px;height:51px;background:var(--footer-3);text-align:center;font:400 12px/51px "Open Sans",sans-serif;color:#ccc}
</style>
</head>
<body>

<header>
  <a class="abs logo" href="#">
    <span class="logo-dot"></span>
    <span class="logo-name">Keystone<br>Mobile Detailing</span>
    <span class="logo-phone">772-555-0148</span>
  </a>
  <div class="abs contact-item" style="left:494px">
    <span class="icon-circle"><svg width="14" height="14" viewBox="0 0 24 24"><path fill="#fff" d="M6.6 10.8a15 15 0 0 0 6.6 6.6l2.2-2.2c.3-.3.7-.4 1-.2 1.1.4 2.3.6 3.6.6.6 0 1 .4 1 1V20c0 .6-.4 1-1 1A17 17 0 0 1 3 4c0-.6.4-1 1-1h3.5c.6 0 1 .4 1 1 0 1.3.2 2.5.6 3.6.1.3 0 .7-.2 1z"/></svg></span>
    <div><div class="contact-label">CALL :</div><a class="contact-value" href="tel:7725550148">772-555-0148</a></div>
  </div>
  <span class="abs divider-v"></span>
  <div class="abs contact-item" style="left:641px">
    <span class="icon-circle"><svg width="14" height="12" viewBox="0 0 24 18"><rect x="1" y="1" width="22" height="16" fill="none" stroke="#fff" stroke-width="2"/><path d="M1 1l11 9 11-9" fill="none" stroke="#fff" stroke-width="2"/></svg></span>
    <div><div class="contact-label">E-MAIL :</div><div class="contact-value">info@keystonemobiledetailing.com</div></div>
  </div>
  <div class="abs socials" aria-label="Social media links"><span></span><span></span><span></span><span></span></div>
</header>

<nav class="abs nav">
  <span class="nav-home"><svg width="18" height="16" viewBox="0 0 24 22"><path fill="#fff" d="M12 1L1 11h3v10h6v-6h4v6h6V11h3z"/></svg></span>
  <a class="active" href="#">Home</a>
  <a href="#">About Us</a>
  <a href="#">Services</a>
  <a href="#">Clients</a>
  <a href="#">Contact Us</a>
  <span class="nav-search"><svg width="15" height="15" viewBox="0 0 24 24"><circle cx="10" cy="10" r="7" fill="none" stroke="#fff" stroke-width="3"/><path d="M15 15l7 7" stroke="#fff" stroke-width="3"/></svg></span>
</nav>

<section>
  <div class="abs hero" role="img" aria-label="Photo of a detailer washing a dark car with a pressure hose inside a garage"></div>
  <h1 class="abs hero-title">we provide this service<br>from 30 years</h1>
  <p class="abs hero-text">Lorem Ipsum is simply dummy text of the printing and typesetting industry. Lorem Ipsum has been the industry's standard dummy text ever</p>
  <a class="abs btn hero-btn" href="#">Contact Us</a>
  <span class="abs hero-arrow" style="left:570px"><svg width="10" height="10" viewBox="0 0 10 10"><path d="M7 1L3 5l4 4" fill="none" stroke="#222" stroke-width="2"/></svg></span>
  <span class="abs hero-arrow" style="left:602px"><svg width="10" height="10" viewBox="0 0 10 10"><path d="M3 1l4 4-4 4" fill="none" stroke="#222" stroke-width="2"/></svg></span>
</section>

<section>
  <p class="abs about-kicker">keystone mobile detailing</p>
  <span class="abs about-rule"></span>
  <h2 class="abs section-title-left">ABOUT US</h2>
  <p class="abs about-text">Lorem Ipsum is simply dummy text of the printing and typesetting industry. Lorem Ipsum has been the industry's standard dummy text ever since the 1500s, when an unknown printer took a galley of type and scrambled it to make a type specimen book. It has survived not only five centuries, but also the leap into electronic typesetting when an unknown printer took a galley of type....</p>
  <div class="abs about-photo" role="img" aria-label="Photo of a detailer washing a white yacht at a marina"></div>
  <a class="abs read-more" href="#">Read More <svg width="18" height="18" viewBox="0 0 18 18"><circle cx="9" cy="9" r="8" fill="none" stroke="#333"/><path d="M5 9h8M10 6l3 3-3 3" fill="none" stroke="#333" stroke-width="1.4"/></svg></a>
</section>

<section>
  <div class="abs services-band"></div>
  <h2 class="abs section-title" style="top:1152px">OUR SERVICES</h2>
  <p class="abs section-sub" style="top:1200px">Lorem Ipsum is simply dummy text of the printing and typesetting industry. Lorem Ipsum has been the industry's standard dummy text ever since the 1500s, when an unknown printer took a galley of type and scrambled it , industry's standard ...</p>
  <div class="abs grid">
    <div class="tile-photo" role="img" aria-label="Photo of a pressure washer spraying a silver car" style="background:linear-gradient(135deg,#c8d4dc,#6d7c88 60%,#3a4550)"></div>
    <div class="tile-text"><h3>Boats</h3><p>Lorem Ipsum is simply dummy text of the printing and typesetting industry. Lorem Ipsum is the industry..</p><a class="more" href="#">READ MORE →</a></div>
    <div class="tile-photo" role="img" aria-label="Photo of a private jet parked at an airport" style="background:linear-gradient(180deg,#9aa8b8,#c9ccd0 55%,#6c6a66)"></div>
    <div class="tile-text"><h3>Car Washing</h3><p>Lorem Ipsum is simply dummy text of the printing and typesetting industry. Lorem Ipsum is the industry..</p><a class="more" href="#">READ MORE →</a></div>
    <div class="tile-photo" role="img" aria-label="Photo of a worker pressure washing the hull of a boat" style="background:linear-gradient(180deg,#e8ecee,#8a9aa2 45%,#2f6b6e 75%,#3a3a3a)"></div>
    <div class="tile-text"><h3>Airplanes</h3><p>Lorem Ipsum is simply dummy text of the printing and typesetting industry. Lorem Ipsum is the industry..</p><a class="more" href="#">READ MORE →</a></div>
  </div>
  <a class="abs btn services-btn" href="#">View More Services</a>
</section>

<section>
  <div class="abs testi-band" role="img" aria-label="Faint dotted world map background"></div>
  <h2 class="abs section-title" style="top:1783px">TESTIMONIALS</h2>
  <div class="abs card" style="left:200px"><p>Lorem Ipsum is simply dummy text of theprinting and typesetting industry. Lor-emIpsum has been the industry's...</p><div class="by">Marla Quinn <span class="stars"><svg width="70" height="12" viewBox="0 0 70 12"><g fill="#f5c518"><path id="s" d="M6 0l1.8 3.9 4.2.4-3.2 2.8 1 4.1L6 9 2.2 11.2l1-4.1L0 4.3l4.2-.4z"/><use href="#s" x="14"/><use href="#s" x="28"/><use href="#s" x="42"/><use href="#s" x="56"/></g></svg></span></div></div>
  <div class="abs card" style="left:472px"><p>Lorem Ipsum is simply dummy text of theprinting and typesetting industry. Lor-emIpsum has been the industry's...</p><div class="by">Marla Quinn <span class="stars"><svg width="70" height="12" viewBox="0 0 70 12"><g fill="#f5c518"><use href="#s"/><use href="#s" x="14"/><use href="#s" x="28"/><use href="#s" x="42"/><use href="#s" x="56"/></g></svg></span></div></div>
  <div class="abs card" style="left:744px"><p>Lorem Ipsum is simply dummy text of theprinting and typesetting industry. Lor-emIpsum has been the industry's...</p><div class="by">Marla Quinn <span class="stars"><svg width="70" height="12" viewBox="0 0 70 12"><g fill="#f5c518"><use href="#s"/><use href="#s" x="14"/><use href="#s" x="28"/><use href="#s" x="42"/><use href="#s" x="56"/></g></svg></span></div></div>
  <div class="abs avatar" style="left:301px" role="img" aria-label="Customer portrait"></div>
  <div class="abs avatar" style="left:573px" role="img" aria-label="Customer portrait"></div>
  <div class="abs avatar" style="left:845px" role="img" aria-label="Customer portrait"></div>
  <div class="abs dots"><span class="on"></span><span></span><span></span></div>
</section>

<section>
  <h2 class="abs section-title" style="top:2171px">OUR CLIENTS</h2>
  <span class="abs client-arrow" style="left:178px"><svg width="10" height="8" viewBox="0 0 10 8"><path d="M9 4H1M4 1L1 4l3 3" fill="none" stroke="#777"/></svg></span>
  <div class="abs client" style="left:227px">Crestline</div>
  <div class="abs client" style="left:379px"><i></i>Oakfield</div>
  <div class="abs client" style="left:537px">Northgate</div>
  <div class="abs client" style="left:687px">Verdano</div>
  <div class="abs client" style="left:839px"><i></i>Millworks</div>
  <span class="abs client-arrow" style="left:1000px"><svg width="10" height="8" viewBox="0 0 10 8"><path d="M1 4h8M6 1l3 3-3 3" fill="none" stroke="#777"/></svg></span>
</section>

<footer>
  <div class="abs footer"></div>
  <div class="abs foot-col" style="left:200px"><h4>Quick Links</h4><ul><li>Home</li><li>About Us</li><li>Services</li><li>Clients</li><li>Contact Us</li></ul></div>
  <div class="abs foot-col" style="left:375px"><h4>Our Services</h4><ul><li>Car Washing</li><li>Car Waxing</li><li>Boat Washing</li><li>Airplane Washing</li><li>Detailing Cars</li></ul></div>
  <div class="abs foot-col" style="left:552px"><h4>Information</h4><ul><li>Site Map</li><li>Help</li><li>Privay Policy</li><li>Term &amp; Conditon</li></ul></div>
  <div class="abs foot-col" style="left:736px"><h4>Newsletter Sign Up</h4></div>
  <div class="abs newsletter">Email Address.. <svg width="20" height="18" viewBox="0 0 24 22"><path fill="#ddd" d="M1 10L23 1l-6 20-5-8z"/></svg></div>
  <div class="abs foot-social" aria-label="Social media links"><span></span><span></span><span></span><span></span></div>

  <div class="abs contact-row"></div>
  <div class="abs cinfo" style="left:145px"><svg width="26" height="28" viewBox="0 0 26 28"><path d="M13 1l11 6.5v13L13 27 2 20.5v-13z" fill="none" stroke="#ccc"/><path d="M13 8a4 4 0 0 0-4 4c0 3 4 7 4 7s4-4 4-7a4 4 0 0 0-4-4z" fill="none" stroke="#ccc" stroke-width="1.4"/></svg>Lorem Ipsum is simply dummy text<br>of the printing</div>
  <div class="abs cinfo" style="left:447px"><svg width="26" height="28" viewBox="0 0 26 28"><path d="M13 1l11 6.5v13L13 27 2 20.5v-13z" fill="none" stroke="#ccc"/><path d="M10 9c-1 1-1 3 1 6s4 4 5 3l1-1-2-2-1 1c-1-.5-2-2-2.5-3l1-1-1.5-2.5z" fill="#ccc"/></svg>Phone : 772-555-0148</div>
  <div class="abs cinfo" style="left:733px"><svg width="26" height="28" viewBox="0 0 26 28"><path d="M13 1l11 6.5v13L13 27 2 20.5v-13z" fill="none" stroke="#ccc"/><rect x="8" y="10" width="10" height="8" fill="none" stroke="#ccc" stroke-width="1.3"/><path d="M8 10l5 4 5-4" fill="none" stroke="#ccc" stroke-width="1.3"/></svg>E-mail : info@keystonemobiledetailing.com</div>
  <div class="abs copy">© Copyright 2018 keystone mobile detailing. All Rights Reserved.</div>
</footer>

</body>
</html>
```